Beautiful Customer Appreciation Gift Box Need Eye Catching Brochure

I need a brochure to include with small sample gift boxes that I send or give to companies who do door to door marketing of businesses, company reps, real estate designers and large companies looking for a unique customer appreciation gifts.

The brochure needs to capture the size variations and the limitless options for their budget and customization needs.

They are gift boxes that can be filled with cookies for the drug rep making an impression for the doc - after cookies are gone, the gift remains

At christmas, we fill them with baked goods and provide to each office. Every year as i visit the offices, they have last years gift box out as a decoration.

realtors can use them as a welcome to your new home gift filled with a bottle of wine and their papers left on the kitchen counter

We have had them used for baby shower gifts, kept later as a decoration.

that's the concept, i need it captured.
Marlow's Festive Nook is the current name
a tag line we came up with is It's all in the WRAPPINGS.
Updates

Project Deadline Extended
Reason: We are very close, I have my photoshoot tomorrow and I'd like to see and continue to tweek the current designs. I have pretty well deleted the designs we are not considering at this point. The others all have components we love. So I need a little more time and some tweaking to decide for sure.

Target Market(s)

the target is the company or individuals looking for gift giving options for clients and customers. From the door to door salesperson looking to make a splash or big impression to the large company looking for nice corporate gift ideas.

The concept of say goodbye to plain jane gift boxes that all look alike... Say goodbye to expensive gift wrap and bows that get thrown away in minutes.... and hello to a beautiful custom made gift box that will remain a decoration or keepsake box forever....

Industry/Entity Type

Retail

Font styles to use
Sans Serif
Script

Requirements
Must have
• IMPORTANT... I CAN and AM GETTING better pictures for the printing purposes. I'm looking more for the concept of the brochuure and layout design.
• I'd love to have it have some place holders for various pictures and descriptions - because each industry targets different people, I'd like to be able to change the front cover of the brochure with a picture of a box that targets that audience a little.
• For a real estate person... i might choose a beautiful centerpiece looking one... vs, the ob/gyn office, I might choose a baby one.
• I have some design skill, just 0 times and the programs have changed alot over the years, so this may go on to future work and a long design relationship as the company grows and changes. I do know photoshop and pagemaker from long ago so I should be able to drop in pics and text options. if we use compatible programs.
Nice to have
• would love to have some kind of background for the page - not just plain white background.
• i like angles and curves
Should not have
• boxy look.

```html
<!DOCTYPE html>
<html lang="en">
<head>
<meta charset="utf-8">
<title>Marlow's Festive Nook – Tri-fold Brochure</title>
<link href="https://fonts.googleapis.com/css2?family=Roboto:wght@400;500;700&display=swap" rel="stylesheet">
<style>
  :root {
    --canvas-bg: #e4e1dd;
    --blue: #0a86c2;
    --blue-deep: #0b4e7e;
    --blue-mid: #0e6da3;
    --orange: #f2a517;
    --orange-deep: #d98a07;
    --paper: #ffffff;
    --paper-shade: #d8d9da;
    --pill: #ececec;
    --ink: #1e1e1e;
  }
  * { box-sizing: border-box; margin: 0; padding: 0; }
  html, body { width: 1200px; height: 875px; overflow: hidden; }
  body {
    background: var(--canvas-bg);
    font-family: 'Roboto', Arial, sans-serif;
    position: relative;
  }
  .brochure {
    position: absolute;
    left: 30px; top: 25px;
    width: 1140px; height: 825px;
    display: flex;
    box-shadow: 0 6px 18px rgba(0,0,0,.25);
  }
  .panel { position: relative; width: 380px; height: 825px; overflow: hidden; }
  .panel-art { position: absolute; inset: 0; width: 380px; height: 825px; }
  .panel > *:not(.panel-art) { position: absolute; }

  /* About panel */
  .about-tab {
    left: 0; top: 36px; width: 162px; height: 38px;
    background: var(--blue); color: #fff;
    border-radius: 0 19px 19px 0;
    font: 700 23px/38px 'Roboto', sans-serif;
    padding-left: 22px;
  }
  .about-copy {
    left: 24px; top: 86px; width: 340px;
    font-size: 12.4px; line-height: 17.6px; color: var(--ink);
  }
  .about-copy p + p { margin-top: 18px; text-align: justify; }
  .thumb-caption {
    top: 724px; width: 180px; text-align: center;
    color: var(--blue-mid); font-weight: 700; font-size: 15px;
  }
  .web-pill {
    left: 45px; top: 764px; width: 290px; height: 48px;
    border-radius: 24px; text-align: center;
    font: 500 19px/48px 'Roboto', sans-serif;
    box-shadow: 0 3px 6px rgba(0,0,0,.3);
  }
  .web-pill.light { background: var(--pill); color: var(--blue-mid); }
  .web-pill.dark { background: var(--blue-mid); color: var(--orange); }

  /* Inside panel */
  .bouquet-photo {
    left: -12px; top: 20px; width: 190px; height: 262px;
    border-radius: 40% 45% 30% 35%;
    background: radial-gradient(circle at 45% 45%, #5b8fd6 0%, #9bc0e8 40%, #e8eef2 70%, rgba(230,236,240,0) 72%);
  }
  .intro-copy {
    right: 22px; top: 36px; width: 240px; text-align: right;
    color: #fff; font-size: 18px; line-height: 24px;
  }
  .contact-title {
    left: 0; width: 380px; top: 648px; text-align: center;
    color: var(--blue-mid); font-size: 28px; font-weight: 500;
  }
  .contact-line {
    left: 0; width: 380px; text-align: center;
    font-size: 15px; color: var(--ink);
    display: flex; justify-content: center; align-items: center; gap: 8px;
  }
  .contact-line svg { width: 13px; height: 13px; }

  /* Cover panel */
  .cover-name {
    left: 0; width: 380px; text-align: center; top: 30px;
    font-weight: 700; font-size: 52px; line-height: 60px; color: var(--orange);
  }
  .cover-sub {
    left: 0; width: 380px; text-align: center; top: 92px;
    font-weight: 500; font-size: 48px; line-height: 58px; color: #fff;
  }
  .cover-headline {
    left: 0; width: 380px; top: 650px; text-align: center;
    color: #fff; font-weight: 700; font-size: 32px; line-height: 46px;
  }
</style>
</head>
<body>
<main class="brochure">

  <!-- About panel -->
  <section class="panel panel-about">
    <svg class="panel-art" viewBox="0 0 380 825" aria-hidden="false">
      <defs>
        <linearGradient id="paperAbout" x1="0" y1="0" x2="1" y2="0">
          <stop offset="0" stop-color="#ffffff"/>
          <stop offset="1" stop-color="#d6d7d8"/>
        </linearGradient>
        <radialGradient id="plantPhoto"><stop offset="0" stop-color="#8a7a52"/><stop offset="1" stop-color="#3f4a2a"/></radialGradient>
        <radialGradient id="rosePhoto"><stop offset="0" stop-color="#e6a3b3"/><stop offset="1" stop-color="#7b5a4a"/></radialGradient>
      </defs>
      <rect width="380" height="825" fill="url(#paperAbout)"/>
      <path d="M0 605 C120 572 260 556 380 568 V760 C260 748 120 752 0 772 Z" fill="var(--orange)"/>
      <path d="M0 592 C120 556 260 540 380 548 V570 C260 560 120 578 0 612 Z" fill="var(--blue)"/>
      <circle cx="99" cy="630" r="70" fill="#fff"/>
      <circle cx="99" cy="630" r="64" fill="url(#plantPhoto)" role="img" aria-label="Photo of a gift box with a green plant arrangement"/>
      <circle cx="285" cy="630" r="70" fill="#fff"/>
      <circle cx="285" cy="630" r="64" fill="url(#rosePhoto)" role="img" aria-label="Photo of a decorated gift box topped with pink roses"/>
    </svg>
    <h2 class="about-tab">About Us</h2>
    <div class="about-copy">
      <p>Lorem ipsum dolor sit amet, consectetuer adipiscing elit. Aenean commodo ligula eget dolor. Aenean massa. Cum sociis natoque penatibus et magnis dis parturient montes, nascetur ridiculus mus. Donec quam felis, ultricies nec, pellentesque eu, pretium quis. Nulla consequat massa quis enim. Donec pede justo, fringilla vel, aliquet nec, vulputate eget, arcu. In enim justo, rhoncus ut, imperdiet a, venenatis vitae, justo. Nullam dictum felis eu pede mollis pretium. Integer tincidunt. Cras dapibus. Vivamus elementum semper nisi. Aenean putate.</p>
      <p>Eleifend tellus. Aenean leo ligula, porttitor eu, consequat vitae, eleifend ac, enim. Aliquam lorem ante, dapibus in, viverra quis, feugiat a, tellus. Phasellus viverra nulla ut metus varius laoreet. Quisque rutrum. Aenean imperdiet. Etiam ultricies nisi vel augiue ullamcorper ultricies nisi. Nam eget dui. Etiam rhoncus. Maecenas tempus, tellus eget condimentum rhoncus, sem quam semper libero, sit amet adipiscing sem neque sed ipsum. Nam quam nunc, blandit vel, luctus pulvinar, hendrerit id, lorem. Maecenas nec odio et ante tincidunt tempus. Donec vitae sapien ut libero venenatis faucibus. Nullam quis ante. Etiam sit amet orci eget eros faucibus tincidunt. Duis leo. Sed fringilla mauris sit amet nibh. Donec sodales sagittis magna. Sed consequat, leo eget bibendum ales, augue velit cursus</p>
    </div>
    <p class="thumb-caption" style="left:9px">Lorem ipsum dolor</p>
    <p class="thumb-caption" style="left:195px">Lorem ipsum dolor</p>
    <p class="web-pill light">www.marlowsfestivenook.com</p>
  </section>

  <!-- Inside panel -->
  <section class="panel panel-inside">
    <svg class="panel-art" viewBox="0 0 380 825">
      <defs>
        <linearGradient id="paperInside" x1="0" y1="0" x2="1" y2="0">
          <stop offset="0" stop-color="#d4d5d6"/>
          <stop offset=".5" stop-color="#ffffff"/>
          <stop offset="1" stop-color="#d4d5d6"/>
        </linearGradient>
        <linearGradient id="blueTop" x1="0" y1="0" x2="1" y2="1">
          <stop offset="0" stop-color="var(--blue)"/>
          <stop offset="1" stop-color="var(--blue-deep)"/>
        </linearGradient>
        <linearGradient id="babyPhoto" x1="0" y1="0" x2="0" y2="1">
          <stop offset="0" stop-color="#b08a9a"/>
          <stop offset=".5" stop-color="#efc6d8"/>
          <stop offset="1" stop-color="#8a7a6a"/>
        </linearGradient>
      </defs>
      <rect width="380" height="825" fill="url(#paperInside)"/>
      <path d="M0 0 H380 V238 C300 244 200 290 0 284 Z" fill="url(#blueTop)"/>
      <path d="M0 284 C200 290 300 244 380 238 V252 C300 258 200 302 0 298 Z" fill="var(--orange)"/>
      <circle cx="193" cy="468" r="134" fill="var(--orange)"/>
      <path d="M80 540 A134 134 0 0 0 320 520 L300 510 A120 120 0 0 1 92 528 Z" fill="var(--blue-mid)"/>
      <circle cx="193" cy="468" r="120" fill="url(#babyPhoto)" role="img" aria-label="Photo of an open baby gift box with a plush toy and pink tissue"/>
      <path d="M0 790 C120 770 260 770 380 790 V825 H0 Z" fill="var(--blue-mid)"/>
    </svg>
    <div class="bouquet-photo" role="img" aria-label="Photo of a blue and white flower bouquet in a decorated box"></div>
    <p class="intro-copy">Lorem ipsum dolor sitamet, consectetuer adipiscing elit. Aenean commodo ligula eet dolor.Cum sociis natoque penati et magnis dis parturient monte</p>
    <h2 class="contact-title">Contact Us</h2>
    <p class="contact-line" style="top:694px">
      <svg viewBox="0 0 16 16"><path d="M3 1h3l1.5 4-2 1.2a9 9 0 0 0 4.3 4.3L11 8.5l4 1.5v3a2 2 0 0 1-2 2A12 12 0 0 1 1 3a2 2 0 0 1 2-2z" fill="var(--orange)"/></svg>
      555 014 2338
    </p>
    <p class="contact-line" style="top:719px">
      <svg viewBox="0 0 16 16"><rect x="1" y="3" width="14" height="10" rx="1" fill="var(--orange)"/><path d="M1.5 4 8 9l6.5-5" fill="none" stroke="#fff" stroke-width="1.3"/></svg>
      info@festivenookmail.com
    </p>
    <p class="web-pill dark">www.marlowsfestivenook.com</p>
  </section>

  <!-- Cover panel -->
  <section class="panel panel-cover">
    <svg class="panel-art" viewBox="0 0 380 825">
      <defs>
        <linearGradient id="coverBlue" x1="0" y1="0" x2="1" y2="1">
          <stop offset="0" stop-color="var(--blue-deep)"/>
          <stop offset=".5" stop-color="var(--blue)"/>
          <stop offset="1" stop-color="var(--blue-deep)"/>
        </linearGradient>
        <linearGradient id="housePhoto" x1="0" y1="0" x2="0" y2="1">
          <stop offset="0" stop-color="#8fc3ec"/>
          <stop offset=".35" stop-color="#dce8f0"/>
          <stop offset=".55" stop-color="#c9b38e"/>
          <stop offset=".75" stop-color="#d9a32a"/>
          <stop offset="1" stop-color="#6d9a3a"/>
        </linearGradient>
      </defs>
      <rect width="380" height="825" fill="url(#coverBlue)"/>
      <path d="M0 238 C120 200 260 178 380 190 V205 C260 195 120 215 0 250 Z" fill="var(--orange)"/>
      <path d="M0 250 C120 215 260 195 380 205 V600 C260 585 120 605 0 640 Z" fill="url(#housePhoto)" role="img" aria-label="Photo of a large family home with a flowering front garden under a blue sky"/>
      <path d="M0 640 C120 605 260 585 380 600 V624 C260 606 120 626 0 666 Z" fill="var(--orange)"/>
    </svg>
    <h1 class="cover-name">MARLOW'S</h1>
    <p class="cover-sub">Festive Nook</p>
    <p class="cover-headline">Lorem ipsum<br>dolor sit amethjas</p>
    <p class="web-pill light">www.marlowsfestivenook.com</p>
  </section>

</main>
</body>
</html>
```